Values Statement poster template

We want to develop a poster template for our company policies and statements which promote our company values in our workplaces.
These documents are important in showing our clients, suppliers and employees who we are and what we stand for.
The graphic design will incorporate our company logo, and be bright, uplifting and inspiring, developing a graphic theme that we can utilise for other company documents. The design will graphically illustrate and support our values statement, with colour and modern design.
This values poster will be the first in a series of documents using the same theme.The format will be a4 and a3 portrait
We are an environmental service business specialising in rehabilitation and revegetation

Target Market(s)

Tier one clients in industry, Mining, Construction and agriculture

Other font styles liked:
• calibri

Requirements
Must have
• Professional , high end feel, able to read clearly on a poster
Nice to have
• graphic design elements, symbols, etc which support the message, that can be carried through to various documents such as quality, environmental, safety policies
A bright theme which ties in with our logo colours.

```html
<!DOCTYPE html>
<html lang="en">
<head>
<meta charset="utf-8">
<title>Verdantis – Values</title>
<link href="https://fonts.googleapis.com/css2?family=Carlito:ital,wght@0,400;0,700;1,400;1,700&display=swap" rel="stylesheet">
<style>
:root{
  --backdrop:#060807;
  --paper:#ffffff;
  --orange:#ff5a00;
  --teal:#44e5d3;
  --lime:#80ff00;
  --green:#1a9a1a;
  --ink:#1b1b1b;
}
*{margin:0;padding:0;box-sizing:border-box}
html,body{width:1200px;height:1200px;overflow:hidden;background:var(--backdrop)}
.stage{width:1333px;height:1333px;transform:scale(0.90023);transform-origin:0 0;position:relative}
.poster{position:absolute;left:238px;top:61px;width:857px;height:1212px;background:var(--paper);overflow:hidden;
  font-family:"Carlito",Calibri,sans-serif;color:var(--ink);font-size:14.2px;line-height:19px}
.band{position:absolute;left:0;width:857px}
.band-top{top:0;height:150px;background:linear-gradient(100deg,var(--orange) 0%,var(--teal) 45%,var(--teal) 70%,var(--lime) 100%)}
.band-bottom{bottom:0;height:90px;background:linear-gradient(100deg,var(--lime) 0%,var(--lime) 40%,var(--teal) 70%,var(--orange) 100%)}
.brand{position:absolute;left:55px;top:190px;display:flex;align-items:center;gap:22px}
.brand-dot{width:62px;height:62px;border-radius:50%;background:var(--orange)}
.brand-name{font-weight:700;font-size:74px;line-height:1;color:var(--green)}
.block{position:absolute}
.left{left:62px;width:360px}
.right{left:470px;width:335px}
.intro b{font-size:17px}
.head{position:relative;font-weight:700;font-size:17px;line-height:20px;text-transform:uppercase}
.head::before{content:"";position:absolute;left:-28px;top:0;border-left:20px solid var(--teal);border-top:10px solid transparent;border-bottom:10px solid transparent}
.head.green{color:var(--green)}
.head.orange{color:var(--orange)}
.sub{font-style:italic}
.lead{margin-top:6px;font-style:italic;font-weight:700;font-size:13.6px}
ul{list-style:none;margin-top:6px}
li{position:relative}
li::before{content:"";position:absolute;left:-16px;top:6px;width:8px;height:8px}
ul.sq-orange li::before{background:var(--orange)}
ul.sq-lime li::before{background:var(--lime)}
ul.spaced li{margin-bottom:6px}
.justify{text-align:justify}
.mark{position:absolute;left:490px;top:800px;width:300px;height:250px}
.mark-dot{position:absolute;left:20px;top:10px;width:190px;height:190px;border-radius:50%;background:var(--teal)}
.mark-name{position:absolute;left:124px;top:212px;font-weight:700;font-size:34px;line-height:1;color:var(--green)}
</style>
</head>
<body>
<div class="stage">
  <div class="poster">
    <div class="band band-top" role="img" aria-label="Decorative header band in orange, teal and lime"></div>
    <div class="band band-bottom" role="img" aria-label="Decorative footer band in lime, teal and orange"></div>

    <div class="brand">
      <span class="brand-dot"></span>
      <span class="brand-name">Verdantis</span>
    </div>

    <div class="block left intro" style="top:318px">
      <p><b>VALUES:</b> These are the things we value most,<br>they define the way we do business</p>
    </div>

    <section class="block left" style="top:372px">
      <h2 class="head green">We value our people</h2>
      <p>above everything else.</p>
      <p class="lead">We demonstrate this by:</p>
      <ul class="sq-orange">
        <li>Providing safe, positive, enjoyable workplaces where everyone feels valued and respected</li>
        <li>Providing Careers, not Jobs, we grow together</li>
        <li>Encouraging inclusion, participation and collaboration</li>
        <li>Recognising and rewarding contribution and excellence</li>
        <li>Supporting our people through tough times</li>
      </ul>
    </section>

    <section class="block left" style="top:569px">
      <h2 class="head orange">We do good things</h2>
      <p class="sub">for the planet</p>
      <p style="margin-top:7px">Our products are helping revegetate Australia, which we are tremendously proud of.</p>
      <p>We minimise our environmental impact in everything we do.</p>
    </section>

    <section class="block left" style="top:681px">
      <h2 class="head green">We set the standard</h2>
      <ul class="sq-lime">
        <li>We are uncompromising on quality</li>
        <li>We are the best at what we do, and we do what we are best at</li>
        <li>We are always improving</li>
        <li>We are pioneering</li>
      </ul>
    </section>

    <section class="block left" style="top:801px">
      <h2 class="head orange">Our workplaces are safe</h2>
      <p class="justify">There is nothing more important to us than our people going home healthy and safe every day. We won’t accept anything less. We believe safety is a management choice. By providing safe work systems, and education we achieve our daily goal of Zero Harm. At Verdantis we;</p>
      <ul class="sq-orange spaced justify" style="margin-top:16px">
        <li>Take the time to make our work areas safe, whatever it takes</li>
        <li>Don’t accept shortcuts</li>
        <li>Look out for each other</li>
        <li>Investigate our incidents and learn from them, we won’t accept repeats</li>
        <li>Are constantly looking for ways to improve the safety of our workplaces.</li>
        <li>Think safe, work safer, go home safe!</li>
      </ul>
    </section>

    <section class="block right" style="top:314px">
      <h2 class="head green">We are proud of who we are</h2>
      <p class="lead" style="margin-top:0">Our reputation means the world to us. We:</p>
      <ul class="sq-lime" style="line-height:20px">
        <li>Treat everyone with respect and we expect it in return</li>
        <li>Follow the rules</li>
        <li>Do what we say we will do</li>
        <li>Own our mistakes and we fix them</li>
        <li>Are trustworthy and transparent</li>
      </ul>
    </section>

    <section class="block right" style="top:496px">
      <h2 class="head orange">We succeed together</h2>
      <p style="line-height:20px">We believe in win-win relationships. When our business is profitable everyone benefits, our owners, employees, clients and the community. At Verdantis we:</p>
      <ul class="sq-orange" style="margin-top:12px;line-height:20px">
        <li>Work as a team, we get it done together</li>
        <li>We treat our suppliers and subcontractors like they are part of the team.</li>
        <li>Are building on our success, and growing together</li>
        <li>Choose to work with employees, customers and suppliers who fit our values</li>
      </ul>
    </section>

    <section class="block right" style="top:729px">
      <h2 class="head green">We give back</h2>
      <p style="line-height:20px">We appreciate our success and we give back by supporting our community, and those less fortunate.</p>
    </section>

    <div class="mark">
      <span class="mark-dot"></span>
      <span class="mark-name">Verdantis</span>
    </div>
  </div>
</div>
</body>
</html>
```